International business needs a web page design

We need a web page design for a new service that our new "sub-company" of our existing company will offer. We are based in Denmark, and our new "sub-company" is called 'Velkari'. The service we offer is automated server configuration and In-Depth monitoring, and optional operations support. Our monitoring has a lot of graphs (like those seen here: https://velkari.example/ with either black or white background ) and the website needs to communicate a sense of Security/safety and that our customers can relax, because we have the full overview of their service and servers. The website should not be with black background.

We deliver low price, high quality and professional operations - which we can do, because we automate it and have people with 15+ years of experience doing so.

We have attached :
a file with our logo : velkari
a file showing the content of the frontage : frontpage
a file showing the content of the user page(for logged in users) : User page
a file showing the pop-up dialog "page" : CallToAction_route
a file showing the 3-steps for the frontpage : 3-step for frontpage

Target Market(s)

Chief Technological officers (CTO's) and Developers (small business, run by developers) - who needs professional IT operations.

Industry/Entity Type

Business

Coding

Coded - Design and coding required

Number of Pages Required

3 page

Requirements
Must have
• Frontpage :
• A lot of visualization(some with people too) rather than a lot of text
• A short, describing text on front page telling what people get
• 3 steps showing people how it works. (Could be presented in a video placed on top of a big front image or perhaps with all 3 steps/pictures shown at the same time or perhaps in a completely different way).
Nice to have
• A big front image(perhaps a person with a cellphone showing graphs and a "all okay" message) with a text and the 3-steps pictures/or video on top of it
• 3 boxes under the front image/top of the site showing what benefits people get from the service
Should not have
• Not a black/dark site

```html
<!DOCTYPE html>
<html lang="en">
<head>
<meta charset="utf-8">
<title>Velkari – Instant Server Setup &amp; In-Depth Monitoring</title>
<link href="https://fonts.googleapis.com/css2?family=Oswald:wght@400;500&family=PT+Sans:ital,wght@0,400;0,700;1,400&display=swap" rel="stylesheet">
<style>
:root{
  --blue:#0a9bd6;
  --blue-dark:#0786bb;
  --navy:#1f2b45;
  --navy-deep:#18223a;
  --ink:#1c2740;
  --text:#3a3f4a;
  --muted:#8a93a3;
  --sand:#e6e4dc;
  --sand-line:#cfccc2;
  --white:#fff;
}
*{margin:0;padding:0;box-sizing:border-box}
html,body{width:857px;height:1200px;overflow:hidden;background:var(--white)}
body{position:relative;font-family:"PT Sans",sans-serif;color:var(--text)}
.abs{position:absolute}
.topbar{left:0;top:0;width:857px;height:16px;background:var(--blue);color:#fff;font-size:5.5px;text-align:right;padding:4px 167px 0 0}
.topbar u{text-decoration:underline}
.navbar{left:0;top:16px;width:857px;height:37px;background:#fff;border-bottom:1px solid #e3e6ea}
.brand{left:167px;top:24px;display:flex;align-items:center;gap:5px}
.brand-dot{width:20px;height:20px;border-radius:50%;background:var(--blue)}
.brand-name{font-size:16px;color:var(--ink);line-height:1}
.brand-sub{font-size:3.5px;color:var(--ink);display:block;margin-top:1px}
.nav{right:168px;top:16px;display:flex;font-size:6px;color:#333;height:37px;align-items:center}
.nav a{padding:0 6.5px;color:inherit;text-decoration:none;height:37px;line-height:37px}
.nav a.active{color:var(--blue);background:#eef6fb}
.hero{left:0;top:53px;width:857px;height:282px;background:radial-gradient(ellipse 260px 170px at 410px 120px,#eeeee5 0%,#c9d3d6 35%,#6f8aa3 65%,#2c3a55 100%);overflow:hidden}
.hero::after{content:"";position:absolute;inset:0;background:radial-gradient(circle 80px at 590px 230px,rgba(120,190,230,.45),transparent)}
.hero-title{top:98px;left:0;width:857px;text-align:center;font-family:"Oswald",sans-serif;font-weight:500;font-size:38px;line-height:43px;color:var(--ink);letter-spacing:-.5px;transform:scaleX(.88)}
.step{width:80px;height:80px;border-radius:50%;top:197px;display:flex;align-items:center;justify-content:center;text-align:center;font-family:"Oswald",sans-serif;font-size:14px;line-height:17px;color:var(--ink);background:rgba(230,232,228,.85);border:2px solid rgba(255,255,255,.8);box-shadow:0 0 0 5px rgba(255,255,255,.25)}
.step.on{background:var(--blue);color:#fff}
.welcome{left:168px;top:312px;width:521px;height:43px;background:var(--sand);border:2px solid #d8d6cd;display:flex;align-items:center;justify-content:space-between;padding:0 12px;font-size:10px;color:var(--ink)}
.btn{background:var(--blue);color:#fff;font-size:10.5px;padding:5px 15px;border:1px solid #fff}
.kicker{font-size:12px;color:var(--ink);line-height:1}
.section-title{font-size:34px;color:var(--blue);line-height:1;letter-spacing:.5px}
.item{display:flex;gap:8px;font-size:5.8px;line-height:10px;width:303px;padding:5px 0 5px 2px}
.item b{color:var(--ink)}
.item.alt{background:var(--sand)}
.ico{flex:none;width:11px;height:11px}
.phones{left:500px;top:370px;width:190px;height:190px;border-radius:10px;background:linear-gradient(90deg,#ef9a99 0 18%,#0a9bd6 30% 70%,#22304d 82%)}
.services{left:0;top:591px;width:857px;height:230px;background:radial-gradient(ellipse 300px 150px at 560px 80px,#e9ece6 0%,#9fb6c5 40%,#3d5273 75%,#26324d 100%);overflow:hidden}
.services .kicker,.services .section-title{color:#fff}
.svc{top:675px;width:120px;height:70px;display:flex;flex-direction:column;align-items:center;justify-content:flex-end;padding-bottom:10px;gap:8px;font-size:10.5px;border:2px solid #fff}
.svc .c{width:28px;height:28px;border-radius:50%;border:1.5px solid currentColor}
.svc.light{background:var(--sand);color:var(--ink)}
.svc.dark{background:var(--blue);color:#fff}
.svc-text{left:167px;top:766px;width:522px;font-size:5.6px;line-height:10.5px;color:#fff}
.arrow-btn{width:15px;height:15px}
.client-card{left:167px;top:913px;width:72px;height:76px;background:var(--sand);border:1px solid var(--sand-line);font-size:4.8px;text-align:center;color:var(--ink)}
.portrait{width:45px;height:45px;margin:12px auto 3px;background:linear-gradient(#6b6b6b,#2a2a2a)}
.quote{left:256px;top:927px;width:434px;font-size:6.3px;line-height:11.5px;font-style:italic;color:var(--ink)}
.divider{left:167px;top:1010px;width:522px;height:2px;background:#eeeeea}
.footer{left:0;top:1039px;width:857px;height:161px;background:var(--navy)}
.footbar{left:0;top:1173px;width:857px;height:27px;background:var(--navy-deep);border-top:1px solid #2d3a58}
.f-h{font-size:8px;color:#fff}
.f-s{font-size:4.6px;line-height:6.5px;color:#aeb6c6}
.email{left:279px;top:1095px;width:143px;height:18px;background:var(--sand);font-size:5.4px;color:#555;padding:6px 7px}
.contact{display:flex;align-items:center;gap:4px;font-size:4.6px;color:#fff}
.social{width:14px;height:14px;border-radius:50%;border:1px solid #aeb6c6}
</style>
</head>
<body>
<div class="abs topbar">Have any questions? Just call us <u>1-555-010-4477</u></div>
<div class="abs navbar"></div>
<div class="abs brand"><span class="brand-dot"></span><div><span class="brand-name">Velkari</span><span class="brand-sub">Instant server setup &amp; in-depth monitoring</span></div></div>
<nav class="abs nav"><a class="active">Home</a><a>About</a><a>How it works</a><a>Services</a><a>Blog</a><a>Gallery</a><a>Help</a><a>Contact</a></nav>

<section class="abs hero" role="img" aria-label="Soft blurred blue and cream light background"></section>
<h1 class="abs hero-title">INSTANT SERVER SETUP &amp;<br>IN-DEPTH MONITORING</h1>
<div class="abs step on" style="left:290px">AUTOMATED<br>SERVER</div>
<div class="abs step" style="left:388px">DEPTH<br>MONITORING</div>
<div class="abs step" style="left:487px">OPERATIONS<br>SUPPORT</div>
<div class="abs welcome"><span><b>Welcome To</b> Velkari</span><span class="btn">Download Brochure</span></div>

<div class="abs kicker" style="left:167px;top:391px">Velkari</div>
<h2 class="abs section-title" style="left:166px;top:401px">WHO WE ARE?</h2>
<div class="abs" style="left:165px;top:445px">
  <div class="item"><svg class="ico" viewBox="0 0 12 12"><circle cx="6" cy="6" r="5.2" fill="none" stroke="#0a9bd6"/><path d="M3.5 6h5M6.5 4l2 2-2 2" fill="none" stroke="#0a9bd6"/></svg><span><b>Our Mission:</b> Nunc sit amet orci sed lorem blandit lobortis quis sed dui. Quisque eget est sem, vel semper purus. Nullam sed lacus eu justo sollicitudin faucibus. Duis gravida semper vehicula.</span></div>
  <div class="item alt" style="margin-top:8px"><svg class="ico" viewBox="0 0 12 12"><circle cx="6" cy="6" r="5.2" fill="none" stroke="#1c2740"/><path d="M3.5 6h5M6.5 4l2 2-2 2" fill="none" stroke="#1c2740"/></svg><span><b>Our vision:</b> Cras at erat nisl. Cras mi orci, aliquet quis tempor et, bibendum a odio. Vivamus eu felis at felis porta pharetra. Praesent mattis enim purus.</span></div>
</div>
<div class="abs phones" role="img" aria-label="Three smartphones showing a server monitoring app"></div>

<section class="abs services" role="img" aria-label="Soft blurred blue light background"></section>
<div class="abs kicker" style="left:167px;top:617px">Available</div>
<h2 class="abs section-title" style="left:166px;top:627px;color:#fff">SERVICES</h2>
<svg class="abs arrow-btn" style="left:650px;top:641px" viewBox="0 0 16 16"><circle cx="8" cy="8" r="7" fill="none" stroke="#e6e4dc" stroke-width="1.5"/><path d="M9.5 5 6 8l3.5 3z" fill="#e6e4dc"/></svg>
<svg class="abs arrow-btn" style="left:672px;top:641px" viewBox="0 0 16 16"><circle cx="8" cy="8" r="7" fill="none" stroke="#1c2740" stroke-width="1.5"/><path d="M6.5 5 10 8l-3.5 3z" fill="#1c2740"/></svg>
<div class="abs svc light" style="left:167px"><span class="c"></span>Automated Server</div>
<div class="abs svc dark" style="left:368px"><span class="c"></span>Online Support</div>
<div class="abs svc dark" style="left:569px"><span class="c"></span>In-Depth Monitering</div>
<p class="abs svc-text"><b>Fusce aliquet euismod luctus.</b> Aliquam scelerisque tincidunt risus nec pellentesque. Cum sociis natoque penatibus et magnis dis parturient montes, nascetur ridiculus mus. Praesent sed tristique massa. Aenean iaculis diam nec ligula ullamcorper eu tempus dolor ullamcorper. Morbi in nisi tincidunt neque gravida facilisis. Pellentesque mattis nisl eget neque scelerisque adipiscing. Vestibulum euismod commodo odio sit amet congue. Donec ut sem vel mauris sodales egestas. Nulla eget lorem vitae diam ullamcorper tincidunt ut vel est.</p>

<div class="abs kicker" style="left:167px;top:861px">Recently</div>
<h2 class="abs section-title" style="left:166px;top:871px">CLIENT SAYS</h2>
<svg class="abs arrow-btn" style="left:650px;top:885px" viewBox="0 0 16 16"><circle cx="8" cy="8" r="7" fill="none" stroke="#0a9bd6" stroke-width="1.5"/><path d="M9.5 5 6 8l3.5 3z" fill="#0a9bd6"/></svg>
<svg class="abs arrow-btn" style="left:672px;top:885px" viewBox="0 0 16 16"><circle cx="8" cy="8" r="7" fill="none" stroke="#e6e4dc" stroke-width="1.5"/><path d="M6.5 5 10 8l-3.5 3z" fill="#e6e4dc"/></svg>
<div class="abs client-card"><div class="portrait" role="img" aria-label="Client portrait photo"></div>Anna Holm</div>
<p class="abs quote">Fusce aliquet euismod luctus. Aliquam scelerisque tincidunt risus nec pellentesque. Cum sociis natoque penatibus et magnis dis parturient montes, nascetur ridiculus mus. Praesent sed tristique massa. Aenean iaculis diam nec ligula ullamcorper eu tempus dolor ullamcorper. Morbi in nisi tincidunt neque gravida facilisis. Pellentesque mattis nisl eget neque scelerisque adipiscing. Vestibulum euismod commodo odio sit amet congue.</p>
<div class="abs" style="left:677px;top:975px;font-size:18px;color:#dcdad2;font-family:Georgia,serif">&ldquo;</div>
<div class="abs divider"></div>

<footer class="abs footer"></footer>
<div class="abs f-h" style="left:167px;top:1069px">News from VELKARI</div>
<p class="abs f-s" style="left:167px;top:1094px;width:110px">Lorem ipsum dolor sit amet, consectetur adipiscing elit. Phasellus sit amet quam augue. Donec ut sem vel mauris sodales egestas.</p>
<div class="abs email">your email here</div>
<svg class="abs" style="left:408px;top:1098px" width="11" height="11" viewBox="0 0 12 12"><circle cx="6" cy="6" r="5.2" fill="none" stroke="#0a9bd6"/><path d="M3.5 6h5M6.5 4l2 2-2 2" fill="none" stroke="#0a9bd6"/></svg>
<div class="abs" style="left:167px;top:1121px;display:flex;gap:14px">
  <span class="contact"><svg width="11" height="11" viewBox="0 0 12 12"><circle cx="6" cy="6" r="5.2" fill="none" stroke="#aeb6c6"/><path d="M4 3.5l1.2 1.4-.6.9a4 4 0 0 0 1.6 1.6l.9-.6 1.4 1.2-.8.9C5.8 8.8 3.2 6.2 3.1 4.3z" fill="#aeb6c6"/></svg>+45 5550 1020</span>
  <span class="contact"><svg width="11" height="11" viewBox="0 0 12 12"><circle cx="6" cy="6" r="5.2" fill="none" stroke="#aeb6c6"/><rect x="3.3" y="4.2" width="5.4" height="3.6" fill="none" stroke="#aeb6c6" stroke-width=".8"/><path d="M3.3 4.2 6 6.2l2.7-2" fill="none" stroke="#aeb6c6" stroke-width=".8"/></svg>info@velkari.example</span>
  <span class="contact"><svg width="11" height="11" viewBox="0 0 12 12"><circle cx="6" cy="6" r="5.2" fill="none" stroke="#aeb6c6"/><path d="M6 9S4 6.6 4 5.2a2 2 0 0 1 4 0C8 6.6 6 9 6 9z" fill="none" stroke="#aeb6c6" stroke-width=".8"/></svg>8 Harbour Lane, Aarhus 8000</span>
</div>
<div class="abs f-h" style="left:568px;top:1069px">Latest Tweets</div>
<div class="abs f-s" style="left:568px;top:1094px;width:122px"><span style="color:var(--blue)">@ velkari</span> Lorem ipsum dolor sit amet, consectetur adipiscing elit. Phasellus sit amet quam augue.<br><i>20 minutes ago</i></div>
<div class="abs f-s" style="left:568px;top:1122px;width:122px"><span style="color:var(--blue)">@ velkari</span> Lorem ipsum dolor sit amet, consectetur adipiscing elit. Phasellus sit amet quam augue.<br><i>1 hour ago</i></div>

<div class="abs footbar"></div>
<div class="abs f-s" style="left:167px;top:1183px">© VELKARI, 2014. All rights reserved.</div>
<div class="abs" style="left:603px;top:1179px;display:flex;gap:6px">
  <span class="social"></span><span class="social"></span><span class="social" style="border-color:var(--blue)"></span><span class="social"></span><span class="social"></span>
</div>
</body>
</html>
```